Book cover for "Generous Horizons" encouraging business to take up compassion pr...

I need a book cover designed for "Generous Horizons. Where Profit Finds Its Heart." The book encourages businesses to take up a social mission (that is, to have a social impact, such as corporate social responsibility.) in doing so, they find a greater sense of purpose, their employees and the community are more engaged, and their business grows. I use stories from my podcast Kindred Venture Hour. 2 key word/phrases that may help t think about are Philanthropy and Corporate Social Responsibility.
This book will be followed by 1 or 2 other books. Another seies of books will also soon requre work.

The market is Mid-sized business owners and CEOs. They have built up the business to a successful place but now find that doesn't bring fulfilment or happiness. The cover needs to have a business or corporate feel.
The Colouring of the book, focus on blues and purples.
This will be a thin book - a quick and easy read of around 110 pages. It is 5x8 inches.
I would be happy to have a photo of me incorporated, but not the focus. I could have a photo done as directed by the designer, as I am planning to have a photoshoot done soon.
Fonts - Please chose a font with the rounded "a", such as in the Century Gothic font, however, open to suggestions.
The back cover will include:
o A book blurb – still to be written
o 2 or 3 endorsements
o Publishing logo (as it is my own publishing company.
o ISBN and barcode
On the spine
• Generous Horizons
• Marisol Tendwick
• Publisher logo icon

For your interest: Marisol is a Speaker, Author, podcaster and Trusted Advisor to Authentic Influencers. Through nourishing community, Marisol maximises the potential of business and influences change.

Target Market(s)

The market is Mid-sized business owners and CEOs. They have built up the business to a successful place but now find that doesn't bring fulfillment or happiness. The cover needs to have a business or corporate feel.

Industry/Entity Type

This is business/corporate book

Font styles to use
Other font styles liked:
• Please chose a font with the rounded "a", such as in the Century Gothic font, however, open to suggestions.

Colors
0054AA
0677BA
7BADD7
CADEEF
E8F1F8
A7469A
B969AE
D3A5CF
EDDBEB
F8F0F9
6B429C
8869AF
B7A5CE
E3DAEB
F3F0F8

Requirements
Must have
• An eye catching design with a business feel.
Nice to have
• I would be nice to edit me into the cover somehow - like Brenmoor puts himself in the background of his movies. I can have photos taken to match .

```html
<!DOCTYPE html>
<html lang="en">
<head>
<meta charset="utf-8">
<title>Generous Horizons — Book Cover</title>
<link rel="stylesheet" href="https://fonts.googleapis.com/css2?family=Bebas+Neue&family=Montserrat:ital,wght@0,300;0,400;0,500;1,800&display=swap">
<style>
  :root {
    --page-bg: #ececec;
    --cover-white: #ffffff;
    --cover-shade: #f1f1f3;
    --title-magenta: #b3197f;
    --band-plum: #80215f;
    --band-plum-deep: #5e1848;
    --band-blue: #0677ba;
    --band-blue-deep: #0054a0;
    --portrait-top: #b9a58e;
    --portrait-mid: #7a2a63;
    --portrait-low: #5a1c4a;
    --text-light: #ffffff;
  }
  html, body {
    margin: 0;
    padding: 0;
    width: 1200px;
    height: 1200px;
    overflow: hidden;
    background: var(--page-bg);
  }
  .canvas {
    position: relative;
    width: 1200px;
    height: 1200px;
  }
  .book-cover {
    position: absolute;
    left: 236px;
    top: 40px;
    width: 728px;
    height: 1120px;
    box-shadow: 0 10px 30px rgba(0,0,0,0.18);
  }
  .book-cover svg { display: block; width: 100%; height: 100%; }
  .title-main {
    font-family: "Bebas Neue", "Oswald", sans-serif;
    fill: var(--title-magenta);
  }
  .title-sub {
    font-family: "Montserrat", sans-serif;
    font-weight: 500;
    fill: var(--title-magenta);
  }
  .author-name {
    font-family: "Montserrat", sans-serif;
    font-weight: 300;
    fill: var(--text-light);
  }
  .tagline {
    font-family: "Montserrat", sans-serif;
    font-weight: 400;
    fill: var(--text-light);
  }
  .tagline .emph { font-weight: 800; font-style: italic; }
</style>
</head>
<body>
<main class="canvas">
  <section class="book-cover" aria-label="Generous Horizons book cover">
    <svg viewBox="0 0 870 1340" xmlns="http://www.w3.org/2000/svg">
      <defs>
        <linearGradient id="coverSheen" x1="0" y1="0" x2="1" y2="1">
          <stop offset="0" stop-color="var(--cover-white)"/>
          <stop offset="0.6" stop-color="var(--cover-shade)"/>
          <stop offset="1" stop-color="var(--cover-white)"/>
        </linearGradient>
        <linearGradient id="plumBand" x1="0" y1="0" x2="1" y2="0">
          <stop offset="0" stop-color="var(--band-plum)"/>
          <stop offset="1" stop-color="var(--band-plum-deep)"/>
        </linearGradient>
        <linearGradient id="blueBand" x1="0" y1="0" x2="1" y2="0.3">
          <stop offset="0" stop-color="var(--band-blue-deep)"/>
          <stop offset="1" stop-color="var(--band-blue)"/>
        </linearGradient>
        <linearGradient id="portraitFill" x1="0" y1="0" x2="0" y2="1">
          <stop offset="0" stop-color="var(--portrait-top)"/>
          <stop offset="0.32" stop-color="var(--portrait-mid)"/>
          <stop offset="1" stop-color="var(--portrait-low)"/>
        </linearGradient>
      </defs>

      <rect class="cover-base" width="870" height="1340" fill="url(#coverSheen)"/>

      <text class="title-main" x="437" y="290" font-size="198" text-anchor="middle" textLength="600" lengthAdjust="spacingAndGlyphs">GENEROUS</text>
      <text class="title-sub" x="437" y="392" font-size="104" text-anchor="middle">horizons</text>

      <polygon class="band-plum" points="0,530 510,775 620,725 620,990 0,720" fill="url(#plumBand)"/>

      <path class="author-portrait" role="img" aria-label="Portrait of the author, smiling, arms folded, wearing a plum dress"
            d="M470,1340 L470,760 Q520,700 600,680 Q610,420 740,400 Q850,420 870,600 L870,1340 Z"
            fill="url(#portraitFill)"/>

      <polygon class="band-blue" points="0,790 540,1055 870,900 870,1140 540,1300 0,1025" fill="url(#blueBand)"/>

      <text class="author-name" x="160" y="712" font-size="40" transform="rotate(26 160 712)">Marisol Tendwick</text>

      <text class="tagline" x="125" y="930" font-size="46" transform="rotate(26 125 930)">where <tspan class="emph">profit</tspan></text>
      <text class="tagline" x="95" y="988" font-size="46" transform="rotate(26 95 988)">finds <tspan class="emph">its heart</tspan></text>
    </svg>
  </section>
</main>
</body>
</html>
```